I need a colour and mono poster design promoting our inaugural concert on December 14th 2013. Venue : The Harwell Chapel. at 6pm. Admission is FREE

The programme we will sing is the 'Garland of Hymns' by Gregory Tamsworth
Accompanied by Marisol Petrak on Concert Harp

I would like the main graphic ie Velmora Children's Choir to look more child-friendly, and imagery childlike drawings. Not babyish but not serious either.

Additional visual information for you : the 26 choristers aged 7-14 years, mixed boys and girls and mixed nationalities wear red robes and are accompanied by a concert harpist.

The final design should attract families and children to attend.

Target Market(s)

Families and Press

Requirements
Must have
• A design that works in reduced format for posting on QZ and other social media

```html
<!DOCTYPE html>
<html lang="en">
<head>
<meta charset="utf-8">
<title>Velmora Children's Choir – Inaugural Concert</title>
<link rel="stylesheet" href="https://fonts.googleapis.com/css2?family=Fredoka:wght@600&family=Lato:wght@300;400;700;900&display=swap">
<style>
  :root {
    --ink: #0b0b0b;
    --paper: #ffffff;
    --paper-mid: #e4e4e4;
    --paper-edge: #b4b4b4;
    --rule: #1a1a1a;
  }
  * { margin: 0; padding: 0; box-sizing: border-box; }
  html, body { width: 887px; height: 1200px; overflow: hidden; background: var(--paper); }
  .poster {
    position: relative;
    width: 887px;
    height: 1200px;
    overflow: hidden;
    background: radial-gradient(ellipse 70% 55% at 50% 52%, var(--paper) 0%, var(--paper-mid) 65%, var(--paper-edge) 100%);
    font-family: 'Lato', sans-serif;
    color: var(--ink);
  }
  .band { position: absolute; left: 0; width: 887px; }
  .band--top { top: 0; height: 215px; }
  .band--bottom { top: 990px; height: 210px; }
  .choir-name {
    position: absolute; top: 36px; left: 0; width: 100%;
    text-align: center;
    font-family: 'Fredoka', sans-serif; font-weight: 600;
    font-size: 60px; line-height: 1; color: var(--paper);
    letter-spacing: 0.5px;
  }
  .choir-illustration {
    position: absolute; left: 83px; top: 208px; width: 717px; height: 380px;
    border-radius: 40px;
    background: radial-gradient(ellipse at center, #f6f6f6 0%, #d6d6d6 70%, rgba(200,200,200,0) 100%);
  }
  .rule { position: absolute; left: 104px; width: 674px; height: 2px; background: var(--rule); }
  .rule--one { top: 609px; }
  .rule--two { top: 817px; }
  .rule--three { top: 892px; }
  .date-month, .date-day, .venue, .time {
    position: absolute; line-height: 1; white-space: nowrap;
  }
  .date-month { left: 102px; top: 624px; font-size: 56px; font-weight: 900; letter-spacing: 0.5px; }
  .date-day { left: 102px; top: 684px; font-size: 55px; font-weight: 400; }
  .time { right: 108px; top: 618px; font-size: 126px; font-weight: 300; letter-spacing: 2px; }
  .venue { left: 0; width: 887px; top: 750px; text-align: center; font-size: 54px; font-weight: 700; letter-spacing: 1.5px; }
  .admission { position: absolute; left: 400px; top: 822px; width: 94px; height: 70px; }
  .programme { position: absolute; left: 0; top: 906px; width: 887px; text-align: center; }
  .programme-heading { font-size: 27px; font-weight: 900; line-height: 34px; letter-spacing: 0.3px; }
  .programme-line { font-size: 25px; font-weight: 300; line-height: 33px; }
  .choir-details {
    position: absolute; left: 0; top: 1088px; width: 887px;
    text-align: center; color: var(--paper);
    font-size: 21px; font-weight: 400; line-height: 29.5px;
    text-transform: uppercase;
  }
</style>
</head>
<body>
<main class="poster">
  <svg class="band band--top" viewBox="0 0 887 215" aria-hidden="true">
    <path d="M0 0 H887 V133 Q443.5 199 0 133 Z" fill="var(--ink)"/>
    <path d="M0 140 Q443.5 206 887 140" fill="none" stroke="var(--ink)" stroke-width="2.5"/>
  </svg>
  <h1 class="choir-name">Velmora Children's Choir</h1>

  <div class="choir-illustration" role="img" aria-label="Line drawing of a group of nine smiling children singing from song sheets, with musical notes around them"></div>

  <div class="rule rule--one"></div>
  <p class="date-month">DECEMBER</p>
  <p class="date-day">14TH 2013</p>
  <p class="time">6PM</p>
  <p class="venue">THE HARWELL CHAPEL</p>
  <div class="rule rule--two"></div>

  <svg class="admission" viewBox="0 0 94 70" aria-label="Admission free">
    <defs>
      <clipPath id="badge-clip"><rect x="0" y="0" width="94" height="70"/></clipPath>
      <path id="badge-arc" d="M16 47 A31 31 0 0 1 78 47"/>
    </defs>
    <circle cx="47" cy="47" r="44" fill="var(--ink)" clip-path="url(#badge-clip)"/>
    <text font-family="Lato, sans-serif" font-weight="700" font-size="14" fill="var(--paper)" letter-spacing="1">
      <textPath href="#badge-arc" startOffset="50%" text-anchor="middle">ADMISSION</textPath>
    </text>
    <text x="47" y="65" text-anchor="middle" font-family="Lato, sans-serif" font-weight="900" font-size="19" fill="var(--paper)" letter-spacing="1">FREE</text>
  </svg>
  <div class="rule rule--three"></div>

  <section class="programme">
    <h2 class="programme-heading">THE PROGRAMME WE WILL SING IS THE:</h2>
    <p class="programme-line">'Garland of Hymns' by Gregory Tamsworth</p>
    <p class="programme-line">Accompanied by Marisol Petrak on Concert Harp</p>
  </section>

  <svg class="band band--bottom" viewBox="0 0 887 210" aria-hidden="true">
    <path d="M0 66 Q443.5 20 887 66" fill="none" stroke="var(--ink)" stroke-width="2.5"/>
    <path d="M0 72 Q443.5 26 887 72 V210 H0 Z" fill="var(--ink)"/>
  </svg>
  <p class="choir-details">
    The 26 choristers aged 7-14 years, mixed boys and girls and<br>
    mixed nationalities wear red robes and are accompanied<br>
    by a concert harpist.
  </p>
</main>
</body>
</html>
```